Bright Pathway! A website showcasing who I am as a person

Bright Pathway started out as idea for me to better myself as a person and work on small projects that would help me grow as a person. Now I want to build a website showcasing "Bright Pathway." I want the website to showcase who I am and how I have grown both professionally and personally. I can build the raw code of the website on my own but I am not really much of a designer. I am looking for a design where I can write and post blogs, articles and share my thoughts. A little about myself and the ideas and interests that I want to share
What is Bright Pathway
Who I am
Background - Professional
Brand Marketing
Email Automation
Hiking
Rock Climbing
Traveling
Exercising and Transformation
"Personal Thoughts"
Hopefully this is enough information to get people started on some designs.
Work
3 page

```html
<!DOCTYPE html>
<html lang="en">
<head>
<meta charset="utf-8">
<title>Bright Pathway</title>
<link href="https://fonts.googleapis.com/css2?family=Open+Sans:wght@400;600;700&family=Ubuntu:wght@400;500;700&display=swap" rel="stylesheet">
<style>
:root{
  --brand:#2a9cc6;
  --brand-dark:#1f86ad;
  --ink:#2b2b2b;
  --text:#6f6f6f;
  --muted:#a9a9a9;
  --line:#e3e3e3;
  --soft:#f3f4f5;
  --white:#ffffff;
  --footer:#222426;
  --footer-text:#bfc3c6;
}
*{margin:0;padding:0;box-sizing:border-box}
html,body{width:1200px;height:4224px;overflow:hidden}
body{font-family:"Open Sans",Arial,sans-serif;color:var(--text);background:var(--white);position:relative}
section,header,footer{position:relative;width:1200px;overflow:hidden}
.abs{position:absolute}
h2.section-title{position:absolute;left:0;width:1200px;text-align:center;font-family:"Ubuntu",Arial,sans-serif;font-weight:500;color:var(--ink);font-size:40px;letter-spacing:1px}
.section-sub{position:absolute;left:0;width:1200px;text-align:center;font-size:15px;color:var(--muted)}
.title-rule{position:absolute;left:540px;width:120px;height:2px;background:var(--line)}

/* header */
.site-header{height:144px;background:var(--white)}
.logo{position:absolute;left:64px;top:44px;font-family:"Ubuntu",Arial,sans-serif;font-weight:500;font-size:44px;color:var(--ink);letter-spacing:1px}
.main-nav{position:absolute;right:60px;top:34px;display:flex;gap:36px;font-size:17px;color:var(--ink)}

/* hero */
.hero{height:346px;background:linear-gradient(90deg,#38b0d6,#2a9cc6 60%,#2592bb)}
.hero-art{position:absolute;left:0;top:0;width:680px;height:346px;background:linear-gradient(120deg,#5cc4e3 0%,#3aa9cf 45%,#2a9cc6 100%)}
.hero-heading{position:absolute;left:800px;top:120px;width:360px;text-align:right;font-family:"Ubuntu",Arial,sans-serif;color:var(--white);line-height:1}
.hero-heading .small{display:block;font-size:66px;font-weight:500;letter-spacing:2px}
.hero-heading .big{display:block;font-size:106px;font-weight:700;letter-spacing:2px}
.hero-badge{position:absolute;left:1060px;top:40px;width:92px;height:70px;border:4px solid var(--white);border-radius:6px}

/* about */
.about{height:680px}
.about-photo{position:absolute;left:64px;top:160px;width:400px;height:490px;background:linear-gradient(160deg,#3c4a56 0%,#1f262d 55%,#0f1317 100%)}
.about-body{position:absolute;left:500px;top:160px;width:640px}
.tabs{display:flex;gap:40px;font-size:15px;font-weight:600;color:var(--ink);border-bottom:2px solid var(--line);padding:0 0 14px 20px}
.tabs span.active{color:var(--brand)}
.about-body p{font-size:16px;line-height:26px;margin-top:26px}
.signature{width:120px;height:40px;margin-top:16px;background:linear-gradient(90deg,#ececec,#d8d8d8)}

/* services */
.services{height:420px;background:var(--soft)}
.service-card{position:absolute;top:130px;width:320px;height:260px;background:var(--white);box-shadow:0 2px 10px rgba(0,0,0,.08);text-align:center;padding:34px 34px 0}
.service-icon{width:60px;height:60px;border-radius:50%;border:2px solid var(--line);margin:0 auto;display:flex;align-items:center;justify-content:center}
.service-card h3{font-size:16px;font-weight:700;color:var(--ink);margin-top:20px;letter-spacing:1px}
.service-card p{font-size:15px;line-height:24px;margin-top:12px}

/* projects */
.projects{height:660px}
.project-tile{position:absolute;width:334px;height:228px}

/* testimonials */
.testimonials{height:440px;background:var(--brand)}
.testimonials h2.section-title{color:var(--white)}
.quote-card{position:absolute;top:150px;width:468px;height:192px;background:var(--white);text-align:center;padding:66px 40px 0}
.quote-avatar{position:absolute;top:-30px;left:204px;width:60px;height:60px;border-radius:50%;border:4px solid var(--white)}
.quote-card p{font-size:14px;line-height:22px}
.quote-card .name{margin-top:14px;font-size:13px;font-weight:700;color:var(--ink)}
.dots{position:absolute;top:384px;left:570px;display:flex;gap:12px}
.dots i{width:10px;height:10px;border-radius:50%;background:rgba(255,255,255,.5)}
.dots i.on{background:var(--white)}

/* blog */
.blog{height:610px}
.post{position:absolute;background:var(--white);box-shadow:0 2px 10px rgba(0,0,0,.08)}
.post h3{font-family:"Ubuntu",Arial,sans-serif;font-weight:700;color:var(--ink);font-size:24px;line-height:30px}
.post p{font-size:13px;line-height:21px;margin-top:12px}
.post-meta{position:absolute;left:28px;right:28px;bottom:22px;display:flex;justify-content:space-between;align-items:center}
.read-more{font-size:11px;font-weight:700;color:var(--ink);letter-spacing:1px}
.share{display:flex;gap:10px}
.share i{width:9px;height:9px;border-radius:50%;background:var(--muted)}

/* cta */
.cta{height:260px;border-top:1px solid var(--line)}
.cta h2{position:absolute;left:0;width:1200px;top:70px;text-align:center;font-family:"Ubuntu",Arial,sans-serif;font-weight:700;color:var(--ink);font-size:40px}
.cta p{position:absolute;left:0;width:1200px;top:128px;text-align:center;font-size:15px;color:var(--muted)}
.btn{position:absolute;background:var(--brand);color:var(--white);font-size:14px;font-weight:600;letter-spacing:1px;display:flex;align-items:center;justify-content:center}

/* contact */
.contact{height:476px;border-top:1px solid var(--line)}
.contact h2{position:absolute;left:64px;top:40px;font-family:"Ubuntu",Arial,sans-serif;font-weight:500;font-size:36px;color:var(--ink);letter-spacing:1px}
.field{position:absolute;border:1px solid var(--line);background:var(--white);font-size:14px;color:var(--text);padding:14px 18px}
.info{position:absolute;left:800px;width:340px}
.info h4{display:flex;align-items:center;gap:12px;font-size:17px;font-weight:700;color:var(--ink)}
.info p{font-size:15px;line-height:24px;margin-top:6px;padding-left:32px}

/* footer */
.site-footer{height:188px;background:var(--footer)}
.footer-nav{position:absolute;left:0;width:1200px;top:40px;display:flex;justify-content:center;gap:38px;font-size:15px;color:var(--footer-text)}
.social{position:absolute;left:0;width:1200px;top:84px;display:flex;justify-content:center;gap:18px}
.social i{width:16px;height:16px;border-radius:50%;background:var(--brand)}
.copyright{position:absolute;left:0;width:1200px;top:126px;text-align:center;font-size:14px;color:var(--footer-text)}
</style>
</head>
<body>

<header class="site-header">
  <div class="logo">BRIGHT PATHWAY</div>
  <nav class="main-nav"><span>Home</span><span>Who I am</span><span>Services</span><span>Gallery</span><span>Blog</span><span>Contact</span></nav>
</header>

<section class="hero">
  <div class="hero-art" role="img" aria-label="Flat illustration of a designer's desktop with monitor, tools and icons"></div>
  <div class="hero-badge"></div>
  <div class="hero-heading"><span class="small">WEB</span><span class="big">DESIGN</span></div>
</section>

<section class="about">
  <h2 class="section-title" style="top:58px">LITTLE STORY ABOUT ME</h2>
  <div class="section-sub" style="top:112px">Know more about me</div>
  <div class="about-photo" role="img" aria-label="Portrait photo of the site owner in a dark jacket"></div>
  <div class="about-body">
    <div class="tabs"><span class="active">DETAILS</span><span>PROFILE</span></div>
    <p>I started Bright Pathway as a quiet promise to myself: take on small projects, learn from each one and grow a little every day. This space collects what I have built, what I have learned and where I am heading next.</p>
    <p>By day I work in brand marketing and email automation, helping small teams find their voice and reach the right people at the right time. Away from the desk I hike, climb rock walls, travel and train, and each of those habits has shaped how I work.</p>
    <p>Here you will find my notes, articles and personal thoughts. Thanks for stopping by.</p>
    <p>Yours sincerely,</p>
    <div class="signature" role="img" aria-label="Handwritten signature"></div>
  </div>
</section>

<section class="services">
  <h2 class="section-title" style="top:50px">MY CREATIVE SERVICES</h2>
  <div class="service-card" style="left:92px">
    <div class="service-icon"><svg width="26" height="20" viewBox="0 0 26 20" fill="none" stroke="#2b2b2b" stroke-width="2"><path d="M8 4 2 10l6 6M18 4l6 6-6 6M15 2l-4 16"/></svg></div>
    <h3>CODING</h3>
    <p>Clean, simple builds for small projects that simply need to work.</p>
  </div>
  <div class="service-card" style="left:440px">
    <div class="service-icon"><svg width="24" height="24" viewBox="0 0 24 24" fill="none" stroke="#2b2b2b" stroke-width="2"><rect x="3" y="5" width="16" height="16"/><path d="M10 14l10-10 2 2-10 10h-2z"/></svg></div>
    <h3>DESIGN</h3>
    <p>Brand looks and layouts that tell a clear and honest story.</p>
  </div>
  <div class="service-card" style="left:788px">
    <div class="service-icon"><svg width="24" height="24" viewBox="0 0 24 24" fill="none" stroke="#2b2b2b" stroke-width="2"><circle cx="12" cy="12" r="9"/><circle cx="12" cy="12" r="4"/><path d="M12 3v5M12 16v5M3 12h5M16 12h5"/></svg></div>
    <h3>SUPPORT</h3>
    <p>Email flows and help that keep your audience close and informed.</p>
  </div>
</section>

<section class="projects">
  <h2 class="section-title" style="top:50px">Latest Projects</h2>
  <div class="section-sub" style="top:106px">See what I have built</div>
  <div class="project-tile" style="left:68px;top:162px;background:linear-gradient(180deg,#e9e9e9 0%,#bdbdbd 45%,#2b2b2b 100%)" role="img" aria-label="Photo of design lettering with pencils"></div>
  <div class="project-tile" style="left:433px;top:162px;background:linear-gradient(135deg,#3a3a3a,#1a1a1a 60%,#555)" role="img" aria-label="Photo of a tablet showing a search page"></div>
  <div class="project-tile" style="left:798px;top:162px;background:linear-gradient(135deg,#efe7dc,#c9b8a4 55%,#8d7b6a)" role="img" aria-label="Photo of a busy desk with a laptop seen from above"></div>
  <div class="project-tile" style="left:68px;top:410px;background:linear-gradient(135deg,#5a5a5a,#2e2e2e 60%,#777)" role="img" aria-label="Photo of a laptop and keyboard on a dark desk"></div>
  <div class="project-tile" style="left:433px;top:410px;background:radial-gradient(circle at 40% 50%,#c0392b 0%,#6a2a6e 35%,#141828 80%)" role="img" aria-label="Photo of colourful blurred lights"></div>
  <div class="project-tile" style="left:798px;top:410px;background:linear-gradient(135deg,#d7c2b3,#a0687f 55%,#5b3b58)" role="img" aria-label="Photo of a tablet and notebook on a desk"></div>
</section>

<section class="testimonials">
  <h2 class="section-title" style="top:52px">Testimonial</h2>
  <div class="quote-card" style="left:112px">
    <div class="quote-avatar" style="background:linear-gradient(135deg,#8aa2b4,#4d6072)" role="img" aria-label="Client portrait"></div>
    <p>Working with him on our email flows was easy. He listens, plans well and the results spoke for themselves within weeks.</p>
    <div class="name">Dana Reyes</div>
  </div>
  <div class="quote-card" style="left:620px">
    <div class="quote-avatar" style="background:linear-gradient(135deg,#d8b48a,#9c7650)" role="img" aria-label="Client portrait"></div>
    <p>A thoughtful marketer with a calm approach. Our brand finally feels clear, and our readers notice the difference.</p>
    <div class="name">Omar Lind</div>
  </div>
  <div class="dots"><i class="on"></i><i></i><i></i></div>
</section>

<section class="blog">
  <h2 class="section-title" style="top:40px">Blog Post</h2>
  <article class="post" style="left:68px;top:118px;width:334px;height:480px">
    <div style="height:240px;background:linear-gradient(180deg,#f4f4f2,#e4e1dc)" role="img" aria-label="Photo of a white desk with a chair"></div>
    <div style="padding:26px 28px 0;text-align:center">
      <h3>Design is not just what it looks like</h3>
      <p>What I learned about design while rebuilding my own site, and why the simple parts matter most in the end.</p>
    </div>
    <div class="post-meta"><span class="read-more">READ MORE</span><span class="share"><i></i><i></i><i></i><i></i></span></div>
  </article>
  <article class="post" style="left:428px;top:118px;width:704px;height:226px">
    <div class="abs" style="left:0;top:0;width:292px;height:226px;background:linear-gradient(135deg,#f7f7f5,#dfe6da)" role="img" aria-label="Photo of a green plant on a white table"></div>
    <div class="abs" style="left:320px;top:28px;width:360px">
      <h3>Beautiful Place for Journey</h3>
      <p>Notes from a long weekend hike, a hard climb and the quiet views that made every step worth it.</p>
    </div>
    <div class="post-meta" style="left:320px"><span class="read-more">READ MORE</span><span class="share"><i></i><i></i><i></i><i></i></span></div>
  </article>
  <article class="post" style="left:428px;top:372px;width:704px;height:226px">
    <div class="abs" style="left:0;top:0;width:292px;height:226px;background:linear-gradient(135deg,#f1efe9,#c8c3b4 60%,#2a2a2a)" role="img" aria-label="Photo of a dark leaf beside a cup"></div>
    <div class="abs" style="left:320px;top:28px;width:360px">
      <h3>Beautiful Place for Journey</h3>
      <p>A short trip that reminded me why slow travel, early mornings and good boots are always worth it.</p>
    </div>
    <div class="post-meta" style="left:320px"><span class="read-more">READ MORE</span><span class="share"><i></i><i></i><i></i><i></i></span></div>
  </article>
</section>

<section class="cta">
  <h2>Wanna Start Work with me?</h2>
  <p>Tell me about your project idea and project brief</p>
  <div class="btn" style="left:500px;top:176px;width:200px;height:44px">START PROJECT</div>
</section>

<section class="contact">
  <h2>CONTACT</h2>
  <div class="field" style="left:68px;top:112px;width:332px;height:50px">Your Name*</div>
  <div class="field" style="left:428px;top:112px;width:332px;height:50px">Your Email*</div>
  <div class="field" style="left:68px;top:192px;width:692px;height:150px">Your Message*</div>
  <div class="btn" style="left:320px;top:382px;width:200px;height:46px;font-size:17px">Submit</div>

  <div class="info" style="top:110px">
    <h4><svg width="20" height="20" viewBox="0 0 20 20"><path d="M10 1a6 6 0 0 0-6 6c0 5 6 12 6 12s6-7 6-12a6 6 0 0 0-6-6z" fill="#2b2b2b"/><circle cx="10" cy="7" r="2.2" fill="#fff"/></svg>Location</h4>
    <p>18 Meadow Lane, Alder Hill,<br>Northbrook - NB4 7QL</p>
  </div>
  <div class="info" style="top:214px">
    <h4><svg width="20" height="20" viewBox="0 0 20 20"><rect x="1" y="4" width="18" height="12" fill="#2b2b2b"/><path d="M1 4l9 7 9-7" fill="none" stroke="#fff" stroke-width="1.5"/></svg>Email</h4>
    <p>hello@brightpathway.example</p>
  </div>
  <div class="info" style="top:290px">
    <h4><svg width="20" height="20" viewBox="0 0 20 20"><path d="M5 1l3 4-2 2c1 3 3 5 6 6l2-2 4 3-2 4C8 18 2 12 1 4z" fill="#2b2b2b"/></svg>Phone</h4>
    <p>+44 (0) 1632 960 418</p>
  </div>
</section>

<footer class="site-footer">
  <nav class="footer-nav"><span>Home</span><span>Who I am</span><span>Services</span><span>Gallery</span><span>Blog</span><span>Contact</span></nav>
  <div class="social"><i></i><i></i><i></i><i></i><i></i><i></i></div>
  <div class="copyright">© 2017 | All Rights Reserved.</div>
</footer>

</body>
</html>
```